Looking for a cool, modern Cannabis Jar Label

I want you to come up with a better, modern look for a label.

I need it sized to 4” x 3” - I plan to print directly to label printer.

I want you to use Photoshop and deliver me a layered PSD file that I can edit and modify the information as needed..

The label information will need to include places for:
(1) Strain Name - most important part of label - larger font size than rest - example Kelvin Thistle, TRP #7, Copperleaf Dunes
(2) Pricing - for Gram, 1/8, 1/4, 1/2. and Ounce
(3) Strain Designation (Hybrid, Indica or Sativa) - maybe color coded, different color for Indica v. Sativa, just an idea
(4) THC and CBD percentages - for example 23% THC and 0.05% CBD
(5) Farm name - a place where we can add the name/logo of the business that produced the product. example - Brosk Farms

I have attached a simple mockup showing the information.

I have also attached a few samples of labels we like to give you an idea of the look and feel we are going for.

I am wanting a very clean, modern, classy, readable look.The font will use is Gotham Font.

HI Everyone! Thank you for all of your designs. I am requesting an extension because I need more time to give adequate feedback to the designers. Thank you for your participation and all of your efforts! I will be making a decision soon!

• Gotham Font

• Thank you for your designs. I am sorry i have been slow in providing feedback, things have been really busy around here!
• I wanted to give some group general feedback. After reviewing all of the designs, there is a common theme among all of the designs that I would like to see changed.
• I would like to see the per gram pricing more prominent on the label. This is what most people are looking for when they are purchasing the product. So I would like to see this stand out from the other pricing tiers. As I think about it, they don't all need to be grouped together in a line. You could have the Per Gram pricing front and center some where and then the other pricing tiers grouped together somewhere else on the label.
• This is the order of importance of items on the label. Items at the the top of the list should be bigger than those below it.
• 1. Strain name
• 2. Pricing - being per gram the most important of all prices
• 3. THC/CBD percentages
• 4. Strain Type (indica, sativa, hybrid)
• 5. Farm name/logo
• When laying out these labels, they will be going on rounded jars and they will be on display. Think of jars with fancy labels in a candy store. They need to be eye catchy, appealing, but easy read.
• Thank you for all of your hard work, everyone is doing a great job.
• Best,
• Neta

```html
<!DOCTYPE html>
<html lang="en">
<head>
<meta charset="utf-8">
<title>Kelvin Thistle – Jar Label</title>
<link rel="stylesheet" href="https://fonts.googleapis.com/css2?family=Montserrat:wght@400;700&display=swap">
<style>
  :root {
    --maroon: #850505;
    --type-tint: #c88a8a;
    --cbd-top: #9e3535;
    --thc-bottom: #a84848;
    --cbd-bottom: #d8aaaa;
    --grown-strip: #cc5555;
    --rule: #dcb4b4;
    --paper: #ffffff;
    --ink: #111111;
  }
  html, body {
    margin: 0;
    width: 1200px;
    height: 917px;
    overflow: hidden;
    background: var(--paper);
    font-family: "Montserrat", sans-serif;
  }
  .label-stage {
    position: absolute;
    left: 0; top: 0;
    width: 1280px;
    height: 978px;
    transform: scale(0.9375);
    transform-origin: 0 0;
  }
  .label {
    position: absolute;
    left: 35px; top: 35px;
    width: 1200px; height: 900px;
    background: var(--maroon);
  }
  .strain-band {
    position: absolute;
    left: 7px; top: 7px;
    width: 1023px; height: 266px;
    background: var(--maroon);
    color: var(--paper);
    text-shadow: 2px 3px 4px rgba(0,0,0,0.45);
  }
  .strain-name {
    position: absolute;
    left: 40px; top: 12px;
    margin: 0;
    font-weight: 400;
    font-size: 116px;
    line-height: 1;
    white-space: nowrap;
  }
  .strain-cross {
    position: absolute;
    left: 44px; top: 148px;
    margin: 0;
    font-weight: 400;
    font-size: 94px;
    line-height: 1;
    white-space: nowrap;
  }
  .strain-type {
    position: absolute;
    left: 1032px; top: 7px;
    width: 161px; height: 266px;
    background: var(--type-tint);
    display: flex;
    align-items: center;
    justify-content: center;
  }
  .strain-type span {
    transform: rotate(-90deg);
    font-size: 60px;
    font-weight: 400;
    color: var(--ink);
    white-space: nowrap;
  }
  .price-panel {
    position: absolute;
    left: 7px; top: 275px;
    width: 1186px; height: 355px;
    background: var(--paper);
  }
  .price-tier {
    position: absolute;
    top: 23px;
    height: 310px;
    border-right: 4px solid var(--rule);
    border-bottom: 4px solid var(--rule);
    box-sizing: border-box;
  }
  .tier-badge {
    position: absolute;
    top: 0;
    width: 146px; height: 146px;
    border-radius: 50%;
    background: var(--maroon);
    color: var(--paper);
    font-size: 64px;
    display: flex;
    align-items: center;
    justify-content: center;
    transform: translateX(-50%);
  }
  .tier-price {
    position: absolute;
    top: 172px;
    left: 0; right: 0;
    text-align: center;
    font-size: 92px;
    color: var(--ink);
    line-height: 1;
    white-space: nowrap;
  }
  .potency {
    position: absolute;
    left: 7px; top: 640px;
    width: 816px; height: 253px;
  }
  .potency svg { position: absolute; left: 0; top: 0; }
  .potency-label {
    position: absolute;
    top: 30px;
    font-weight: 700;
    font-size: 62px;
    color: var(--paper);
    text-shadow: 2px 3px 4px rgba(0,0,0,0.4);
    transform: translateX(-50%);
  }
  .potency-value {
    position: absolute;
    top: 140px;
    font-size: 104px;
    line-height: 1;
    white-space: nowrap;
    transform: translateX(-50%);
  }
  .potency-value sup { font-size: 48px; vertical-align: 44px; margin-left: 2px; }
  .thc-value { color: var(--paper); text-shadow: 2px 3px 4px rgba(0,0,0,0.4); }
  .cbd-value { color: var(--ink); }
  .grower {
    position: absolute;
    left: 830px; top: 640px;
    width: 363px; height: 253px;
    background: var(--paper);
  }
  .grower-heading {
    height: 60px;
    background: var(--grown-strip);
    color: var(--ink);
    font-size: 44px;
    text-align: center;
    line-height: 60px;
  }
  .grower-name {
    height: 193px;
    display: flex;
    align-items: center;
    justify-content: center;
    gap: 18px;
    font-weight: 700;
    font-size: 40px;
    color: var(--ink);
  }
  .grower-name i {
    width: 50px; height: 50px;
    border: 3px solid var(--ink);
    border-radius: 50%;
  }
</style>
</head>
<body>
<div class="label-stage">
  <div class="label">
    <header class="strain-band">
      <h1 class="strain-name">Kelvin Thistle</h1>
      <h2 class="strain-cross">Copperleaf Dunes</h2>
    </header>
    <div class="strain-type"><span>Hybrid</span></div>

    <section class="price-panel">
      <div class="price-tier" style="left:18px;width:173px"><div class="tier-badge" style="left:75px">g.</div><div class="tier-price">$10</div></div>
      <div class="price-tier" style="left:216px;width:186px"><div class="tier-badge" style="left:88px">1/8</div><div class="tier-price">$35</div></div>
      <div class="price-tier" style="left:430px;width:192px"><div class="tier-badge" style="left:89px">1/4</div><div class="tier-price">$70</div></div>
      <div class="price-tier" style="left:648px;width:232px"><div class="tier-badge" style="left:111px">1/2</div><div class="tier-price">$140</div></div>
      <div class="price-tier" style="left:908px;width:258px"><div class="tier-badge" style="left:121px">Oz</div><div class="tier-price">$280</div></div>
    </section>

    <section class="potency">
      <svg width="816" height="253" viewBox="0 0 816 253">
        <rect x="0" y="0" width="816" height="125" fill="var(--maroon)"/>
        <polygon points="318,0 816,0 816,125 390,125" fill="var(--cbd-top)"/>
        <rect x="0" y="127" width="816" height="126" fill="var(--thc-bottom)"/>
        <polygon points="391,127 816,127 816,253 460,253" fill="var(--cbd-bottom)"/>
      </svg>
      <div class="potency-label" style="left:155px">THC</div>
      <div class="potency-label" style="left:586px">CBD</div>
      <div class="potency-value thc-value" style="left:170px">28<sup>%</sup></div>
      <div class="potency-value cbd-value" style="left:604px">0.05<sup>%</sup></div>
    </section>

    <aside class="grower">
      <div class="grower-heading">Grown by</div>
      <div class="grower-name"><i></i>Brosk Farms</div>
    </aside>
  </div>
</div>
</body>
</html>
```